Organic lawn care

take the same sign as the mosquito sign, only instead of the mosquito image have the red circle and line cross out the text of "chemicals". Have the sign say "this lawn receives ORGANIC grass treatments" "instantly SAFE for people and pets"

Lawn Care

```html
<!DOCTYPE html>
<html lang="en">
<head>
<meta charset="utf-8">
<title>Organic Lawn Care Sign</title>
<link rel="stylesheet" href="https://fonts.googleapis.com/css2?family=Quicksand:wght@500;600&family=Montserrat:wght@800&display=swap">
<style>
  :root {
    --lawn-green: #005f27;
    --sign-white: #ffffff;
    --prohibit-red: #e30613;
    --ink: #111111;
    --flask-tone: #d9d9d9;
  }
  html, body {
    margin: 0;
    padding: 0;
    overflow: hidden;
    background: var(--sign-white);
  }
  .sign {
    position: relative;
    width: 1200px;
    height: 1200px;
    background: var(--sign-white);
    overflow: hidden;
    font-family: "Quicksand", sans-serif;
  }
  .band {
    position: absolute;
    left: 0;
    width: 1200px;
    background: var(--lawn-green);
    color: var(--sign-white);
    display: flex;
    align-items: center;
    justify-content: center;
    text-align: center;
    font-weight: 600;
  }
  .band--top {
    top: 0;
    height: 222px;
  }
  .band--bottom {
    top: 982px;
    height: 218px;
  }
  .headline {
    margin: 0;
    font-size: 66px;
    line-height: 88px;
    font-weight: 600;
    letter-spacing: 0.5px;
  }
  .tagline {
    margin: 0;
    font-size: 62px;
    font-weight: 600;
    letter-spacing: 0.5px;
  }
  .prohibit {
    position: absolute;
    left: 0;
    top: 0;
    width: 1200px;
    height: 1200px;
  }
  .flask-area {
    fill: var(--flask-tone);
  }
  .flask-label {
    font-family: "Montserrat", sans-serif;
    font-weight: 800;
    font-size: 45px;
    fill: var(--ink);
    letter-spacing: 1px;
  }
  .prohibit-ring,
  .prohibit-slash {
    fill: none;
    stroke: var(--prohibit-red);
    stroke-width: 39;
  }
</style>
</head>
<body>
  <main class="sign">
    <header class="band band--top">
      <h1 class="headline">This lawn receives ORGANIC<br>grass treatments</h1>
    </header>

    <svg class="prohibit" viewBox="0 0 1200 1200" xmlns="http://www.w3.org/2000/svg">
      <rect class="flask-area" x="395" y="352" width="417" height="463" rx="40"
            role="img" aria-label="Laboratory flask with bubbles, labelled chemicals"/>
      <text class="flask-label" x="598" y="765" text-anchor="middle">CHEMICALS</text>
      <circle class="prohibit-ring" cx="596" cy="598" r="324"/>
      <line class="prohibit-slash" x1="345" y1="768" x2="846" y2="425"/>
    </svg>

    <footer class="band band--bottom">
      <p class="tagline">Instantly SAFE for people and pets</p>
    </footer>
  </main>
</body>
</html>
```